Events By Halvane

Weddings, Corporate, Special Events
Memorable Catering, Personalized Menus, Custom Layout & Designs
Professional Staff, Excellent Service
Our Mission is Turning YOUR Vision into a Reality

Odette Halvane, Principal Planner
ph. 202 418-7352 - fax 301-847-2951
Email - eventsbyhalvane@mailtrove.com
Web - www.cateringbyhalvane.com
cateringbyhalvane@Instagram

Target Market(s)

All Brides, Corprate Business, Special Events

Industry/Entity Type

Hospitality

Contact Information for Business Card

clean but affective

Font styles to use
Serif
Sans Serif
Script

Colors

Designer to choose colors to be used in the design.

Requirements
Must have
• logo with tagline using colors that will enhance what
• some pictures of nice table scape, hors d'oevures, upscale foods......
Nice to have
• Event: Something that happens or is regarded as happening, an occurrence especially one of some importance.
Should not have
• Use Logo on both sides

```html
<!DOCTYPE html>
<html lang="en">
<head>
<meta charset="utf-8">
<title>Events By Halvane – Business Card</title>
<link rel="stylesheet" href="https://fonts.googleapis.com/css2?family=Cinzel:wght@400;600&family=Raleway:ital,wght@0,400;0,500;1,500;1,700&display=swap">
<style>
  :root {
    --page: #e6e6e6;
    --teal: #1fa9b5;
    --ink: #211e1f;
    --white: #ffffff;
    --grey: #8c8c8c;
    --ring: #9a9a9a;
    --gap: #3a3a3a;
  }
  * { margin: 0; padding: 0; box-sizing: border-box; }
  html, body { width: 1200px; height: 960px; overflow: hidden; background: var(--page); }
  .canvas { position: relative; width: 1200px; height: 960px; }

  .card { position: absolute; left: 311px; width: 600px; height: 343px; overflow: hidden;
          box-shadow: 0 2px 5px rgba(0,0,0,.35); }
  .card-front { top: 111px; background: var(--white); }
  .card-back { top: 472px; background: var(--ink); }

  .front-art { position: absolute; inset: 0; }

  .planner { position: absolute; left: 34px; top: 48px; color: var(--white); text-align: center; width: 214px; }
  .planner-name { font-family: 'Cinzel', serif; font-size: 25px; font-weight: 400; letter-spacing: .5px; }
  .planner-role { font-family: 'Raleway', sans-serif; font-size: 15px; letter-spacing: 2.2px; margin-top: 2px; }

  .contacts { position: absolute; left: 36px; top: 216px; list-style: none;
              font-family: 'Raleway', sans-serif; font-size: 14px; color: var(--white); line-height: 19.2px; }
  .contacts li { display: flex; align-items: center; gap: 6px; }
  .contacts svg { width: 11px; height: 11px; fill: var(--teal); flex: none; }

  .brand { position: absolute; text-align: center; }
  .brand-ring { display: block; margin: 0 auto; border: 3px solid var(--ring); border-radius: 50%; }
  .brand-name { font-family: 'Cinzel', serif; font-weight: 600; color: var(--teal); white-space: nowrap; }
  .brand-tag { font-family: 'Cinzel', serif; color: var(--grey); white-space: nowrap; }

  .brand-front { left: 312px; top: 86px; width: 234px; }
  .brand-front .brand-ring { width: 74px; height: 74px; margin-bottom: 26px; }
  .brand-front .brand-name { font-size: 22px; }
  .brand-front .brand-tag { font-size: 9.5px; margin-top: 2px; }

  .brand-back { left: 22px; top: 28px; width: 190px; }
  .brand-back .brand-ring { width: 64px; height: 64px; margin-bottom: 22px; }
  .brand-back .brand-name { font-size: 18px; }
  .brand-back .brand-tag { font-size: 8px; margin-top: 1px; color: #bdbdbd; }

  .services { position: absolute; left: 26px; top: 165px; list-style: none;
              font-family: 'Raleway', sans-serif; font-style: italic; font-weight: 500;
              font-size: 16px; color: var(--teal); line-height: 22px; }
  .services li { display: flex; align-items: center; gap: 7px; }
  .services svg { width: 18px; height: 12px; fill: var(--teal); }

  .mission-band { position: absolute; left: 0; top: 295px; width: 327px; height: 28px; background: var(--teal);
                  font-family: 'Raleway', sans-serif; font-style: italic; font-weight: 700; font-size: 14.5px;
                  color: var(--white); line-height: 28px; padding-left: 26px; }
  .band-end { position: absolute; left: 583px; top: 295px; width: 17px; height: 28px; background: var(--teal); }
  .rule { position: absolute; top: 0; width: 3px; height: 343px; background: var(--teal); }
  .rule-left { left: 330px; }
  .rule-right { left: 575px; }

  .gallery { position: absolute; left: 336px; top: 0; width: 236px; height: 343px; background: var(--gap);
             display: grid; grid-template-columns: 114px 114px; grid-template-rows: 108px 110px 110px;
             gap: 7px 5px; padding-left: 3px; }
  .photo { display: block; }
  .p1 { background: linear-gradient(135deg, #e9e4df, #b8474a 55%, #5f8f3a); }
  .p2 { background: linear-gradient(135deg, #f2efe9, #d8b24a 40%, #5a3a2d); }
  .p3 { background: linear-gradient(135deg, #6d4b22, #c8883a 45%, #e6d9c2); }
  .p4 { background: linear-gradient(135deg, #2f3a1f, #c2452c 50%, #e09a6a); }
  .p5 { background: linear-gradient(135deg, #2a2620, #c99a5e 50%, #4f6b2a); }
  .p6 { background: linear-gradient(135deg, #e8ecef, #9aa6ad 50%, #3f5a2a); }
</style>
</head>
<body>
<main class="canvas">

  <section class="card card-front" aria-label="Business card front">
    <svg class="front-art" viewBox="0 0 600 343" width="600" height="343">
      <defs>
        <linearGradient id="photoTop" x1="0" y1="0" x2="1" y2="1">
          <stop offset="0" stop-color="#5a5350"/>
          <stop offset=".6" stop-color="#3b3635"/>
          <stop offset="1" stop-color="#2a2626"/>
        </linearGradient>
        <linearGradient id="photoBottom" x1="0" y1="0" x2="1" y2="1">
          <stop offset="0" stop-color="#3f3c40"/>
          <stop offset=".5" stop-color="#2c2a2c"/>
          <stop offset="1" stop-color="#1f1e1f"/>
        </linearGradient>
      </defs>
      <g role="img" aria-label="Photo of a bride and groom holding hands with a bouquet of white roses">
        <path d="M0,0 H385 C330,20 302,62 298,108 C294,150 282,166 250,169 H0 Z" fill="url(#photoTop)"/>
      </g>
      <g role="img" aria-label="Photo of an elegant table setting with glassware and flowers">
        <path d="M0,175 H250 C282,178 290,210 298,250 C308,298 326,328 342,343 H0 Z" fill="url(#photoBottom)"/>
      </g>
    </svg>

    <div class="planner">
      <h1 class="planner-name">Odette Halvane</h1>
      <p class="planner-role">PRINCIPAL PLANNER</p>
    </div>

    <ul class="contacts">
      <li><svg viewBox="0 0 12 12"><path d="M2.5 1 L4.5 1 L5.2 3.6 L4 4.6 C4.6 6 5.9 7.4 7.4 8 L8.4 6.8 L11 7.5 L11 9.5 C11 10.4 10.3 11 9.4 11 C5 10.6 1.4 7 1 2.6 C1 1.7 1.6 1 2.5 1 Z"/></svg>(202 418-7352)</li>
      <li><svg viewBox="0 0 12 12"><rect x="3" y="1" width="6" height="3"/><rect x="0.5" y="4.5" width="11" height="5" rx="1"/><rect x="3" y="8" width="6" height="3"/></svg>(301-847-2951)</li>
      <li><svg viewBox="0 0 12 12"><path d="M0.5 2.5 H11.5 V9.5 H0.5 Z M1.2 3 L6 6.6 L10.8 3"/></svg>eventsbyhalvane@mailtrove.com</li>
      <li><svg viewBox="0 0 12 12"><circle cx="6" cy="6" r="5.5"/></svg>www.eventsbyhalvane.com</li>
      <li><svg viewBox="0 0 12 12"><rect x="0.5" y="0.5" width="11" height="11" rx="2.5"/></svg>@eventsbyhalvane</li>
    </ul>

    <div class="brand brand-front">
      <span class="brand-ring" aria-hidden="true"></span>
      <p class="brand-name">Events By Halvane</p>
      <p class="brand-tag">Events Designed with You in mind</p>
    </div>
  </section>

  <section class="card card-back" aria-label="Business card back">
    <div class="brand brand-back">
      <span class="brand-ring" aria-hidden="true"></span>
      <p class="brand-name">Events By Halvane</p>
      <p class="brand-tag">Events Designed with You in mind</p>
    </div>

    <ul class="services">
      <li><svg viewBox="0 0 18 12"><path d="M0 6 L9 1 L18 6 L9 11 Z"/></svg>Weddings, Corporate</li>
      <li><svg viewBox="0 0 18 12"><path d="M0 6 L9 1 L18 6 L9 11 Z"/></svg>Special Events</li>
      <li><svg viewBox="0 0 18 12"><path d="M0 6 L9 1 L18 6 L9 11 Z"/></svg>Personalized Menus &amp; Designs</li>
      <li><svg viewBox="0 0 18 12"><path d="M0 6 L9 1 L18 6 L9 11 Z"/></svg>Professional Staff</li>
      <li><svg viewBox="0 0 18 12"><path d="M0 6 L9 1 L18 6 L9 11 Z"/></svg>Great Service</li>
    </ul>

    <p class="mission-band">TURNING YOUR VISION INTO A REALITY</p>

    <span class="rule rule-left" aria-hidden="true"></span>
    <div class="gallery">
      <span class="photo p1" role="img" aria-label="Photo of seared tuna with micro greens"></span>
      <span class="photo p2" role="img" aria-label="Photo of grilled steak with vegetables"></span>
      <span class="photo p3" role="img" aria-label="Photo of roasted chicken in sauce"></span>
      <span class="photo p4" role="img" aria-label="Photo of salmon fillet with garnish"></span>
      <span class="photo p5" role="img" aria-label="Photo of seared scallops"></span>
      <span class="photo p6" role="img" aria-label="Photo of plated hors d'oeuvres on a banquet table"></span>
    </div>
    <span class="rule rule-right" aria-hidden="true"></span>
    <span class="band-end" aria-hidden="true"></span>
  </section>

</main>
</body>
</html>
```